An expert for Professional and Technical Evaluation of Painting Work Needs a New Letterhead Design

I own a mid-sized painting company and also work as an expert for professional and technical evaluation of painting work in the area of Zurich.

Please read the project description and the must-have-requirements carefully!

I attached 1 PDF which will help you create a new letterhead design:

THE NEW DESIGN DOESN'T NEED A LOGO! (Because it won't represent a company, it represents only a service)
Updates

Dear designers We had a discussion about the location/placement of the design and came to the conclusion that we only want the design to be in the header area of the A4-paper. We would be glad to receive some revised version of your designs. Thank you and kind regards!

Reason: Due to the fact that only 20% of the designer have understood the brief and submitted designs that have met the requirements we decided to extend the contest deadline.

Reason: A great deal of good designs were submitted in the last few days. A big thank you to all the participating designers for your good work. We need a few more days to discuss some changes with certain designers and to decide which design will win.

Target Market(s)

(Insurance) Companies, partly also private clients.

Industry/Entity Type

Painting

Colors

Designer to choose colors to be used in the design.

Requirements
Must have
• All information (text, phone numbers, ...) of the old design ("old_letterhead_design.pdf") has also to be in the new one. Additional to that there are a few changes:
The phone numbers "01 583 61 47" and "01 583 61 37" change to "044 583 61 47" and "044 583 61 37". And please mention also this email address: gutachten@holvantrek.example .

- The design should only be in the header-area of the A4-paper. An the background color of the A4-paper will be white.

- The design should consist of two designs. One for the first page and a smaller version of the design for the following pages.

- THE NEW DESIGN DOESN'T NEED A LOGO! You can make a design with geometric forms, ...

- The new design should have a juridical look. It should only contain colors like brown, fawn, black, light green, ...... colors which look serious/reliable.
Nice to have
• Geometric Forms, Symbols or other design elements.

- It would also be nice to have some design elements which emphasize the kind of work we are offering.

```html
<!DOCTYPE html>
<html lang="de">
<head>
<meta charset="utf-8">
<title>Erwin Holvantrek – Briefbogen Erstseite und Folgeseite</title>
<link rel="stylesheet" href="https://fonts.googleapis.com/css2?family=Lato:wght@400;900&display=swap">
<style>
  :root {
    --backdrop: #8f8f8f;
    --paper: #ffffff;
    --navy: #3a4f80;
    --ink: #2d2d35;
  }
  * { box-sizing: border-box; margin: 0; padding: 0; }
  html, body { width: 1200px; height: 640px; overflow: hidden; }
  body {
    background: var(--backdrop);
    font-family: "Lato", Arial, sans-serif;
    color: var(--ink);
    position: relative;
  }
  .sheet {
    position: absolute;
    top: 40px;
    width: 396px;
    height: 560px;
    background: var(--paper);
    box-shadow: 0 2px 6px rgba(0,0,0,.25);
    overflow: hidden;
  }
  .sheet--first { left: 150px; }
  .sheet--following { left: 654px; }
  .sheet__topline {
    position: absolute; top: 0; left: 0; right: 0;
    height: 4px; background: var(--navy);
  }
  .brand {
    position: absolute; left: 28px; top: 30px;
    display: flex; align-items: center; gap: 6px;
    color: var(--navy); font-weight: 900;
  }
  .brand__square { width: 22px; height: 22px; background: var(--navy); flex: none; }
  .brand__name { font-size: 11px; letter-spacing: .2px; white-space: nowrap; }
  .sheet--following .brand { top: 26px; gap: 5px; }
  .sheet--following .brand__square { width: 16px; height: 16px; }
  .sheet--following .brand__name { font-size: 8.5px; }

  .contact {
    position: absolute; right: 24px; top: 30px;
    display: flex; gap: 5px;
    font-size: 5.6px; line-height: 9px;
    white-space: nowrap;
  }
  .contact__services { list-style: none; text-align: right; }
  .contact__services li::after {
    content: ""; display: inline-block;
    width: 4px; height: 4px; border-radius: 50%;
    background: var(--navy); margin-left: 3px; vertical-align: middle;
  }
  .contact__divider { width: 1px; background: var(--navy); }
  .contact__details { list-style: none; }
  .contact__details li { display: flex; align-items: center; gap: 3px; height: 9px; }
  .contact__details svg { width: 6px; height: 6px; flex: none; }
</style>
</head>
<body>

<section class="sheet sheet--first" aria-label="Briefbogen Erstseite">
  <div class="sheet__topline"></div>
  <div class="brand">
    <span class="brand__square"></span>
    <span class="brand__name">Erwin Holvantrek</span>
  </div>
  <div class="contact">
    <ul class="contact__services">
      <li>Gutachten</li>
      <li>Expertisen</li>
      <li>Bewertungen</li>
      <li>Farbberatungen</li>
      <li>Dekorative Gestaltungen</li>
    </ul>
    <div class="contact__divider"></div>
    <ul class="contact__details">
      <li><svg viewBox="0 0 10 10"><circle cx="5" cy="5" r="4.5" fill="none" stroke="#3a4f80"/><path d="M3 2.5 L4.3 2.5 L4.8 4 L4 4.6 Q4.8 6 6 6.4 L6.6 5.6 L7.8 6.2 L7.6 7.5 Q4 7.5 3 3.6 Z" fill="#3a4f80"/></svg>044 583 61 47</li>
      <li><svg viewBox="0 0 10 10"><circle cx="5" cy="5" r="4.5" fill="none" stroke="#3a4f80"/><rect x="2.8" y="3" width="4.4" height="4" fill="#3a4f80"/></svg>044 583 61 37</li>
      <li><svg viewBox="0 0 10 10"><circle cx="5" cy="5" r="4.5" fill="none" stroke="#3a4f80"/><rect x="2.5" y="3.2" width="5" height="3.6" fill="none" stroke="#3a4f80" stroke-width=".8"/><path d="M2.5 3.2 L5 5.2 L7.5 3.2" fill="none" stroke="#3a4f80" stroke-width=".8"/></svg>gutachten@holvantrek.example</li>
      <li><svg viewBox="0 0 10 10"><circle cx="5" cy="5" r="4.5" fill="#3a4f80"/></svg>eidg. dipl. Malermeister</li>
    </ul>
  </div>
</section>

<section class="sheet sheet--following" aria-label="Briefbogen Folgeseite">
  <div class="sheet__topline"></div>
  <div class="brand">
    <span class="brand__square"></span>
    <span class="brand__name">Erwin Holvantrek</span>
  </div>
</section>

</body>
</html>
```